Bluestone Advisory & Mgmt - Professional Business Cards

Hi!

I am a Real Estate Developer and Construction Consultant.

I have a lot of inspiration from previous designs and would be open to using the attached Designs as a starting point. I would like to see these styles incorporated into your designs.

I really need professional business card to go with it that includes my important info.

Look forward to seeing your designs!.

Target Market(s)

My Target market are building owners, lawyers, consultants.

Industry/Entity Type

Real Estate Development

Contact Information for Business Card

My Name: Dorian Pelkey
My Title: Principle
Company Name: Bluestone Advisory & Mgmt, LLC
Address: 348 West 71st Street, 9th FL New York, NY 10010
Mobile: 917.806.3971
Website: bam-hvx.example

Font styles to use
Serif
Sans Serif

Colors

Designer to choose colors to be used in the design.

Requirements
Must have
• Must incorporate the logo attached or have new that looks similar.
• Must use professional font that will be seen and judged by wealthy land owners and developers.
• Must incorporate some of the color green.
Should not have
• Photo's or pictures of people or buildings of any kind.

```html
<!DOCTYPE html>
<html lang="en">
<head>
<meta charset="utf-8">
<title>Bluestone Advisory &amp; Mgmt – Business Cards</title>
<link rel="stylesheet" href="https://fonts.googleapis.com/css2?family=Poppins:wght@300;400;500;600&display=swap">
<style>
  :root {
    --brand-green: #4bb77a;
    --brand-green-deep: #2f9e5c;
    --brand-grey: #9b9490;
    --ink-grey: #6f6a67;
    --card-white: #fbfbfb;
    --backdrop: #e7e8e7;
    --line-white: rgba(255,255,255,0.85);
  }
  * { box-sizing: border-box; margin: 0; padding: 0; }
  html, body {
    width: 1200px; height: 900px; overflow: hidden;
    background: var(--backdrop);
    font-family: "Poppins", Arial, sans-serif;
  }
  .sheet {
    width: 1200px; height: 900px;
    display: flex; flex-direction: column; align-items: center; justify-content: center;
    gap: 56px;
  }
  .card {
    position: relative;
    width: 640px; height: 366px;
    box-shadow: 0 10px 28px rgba(0,0,0,0.16);
    overflow: hidden;
  }

  /* Front */
  .card--front { background: var(--card-white); }
  .front__edge { position: absolute; left: 0; bottom: 0; width: 640px; height: 18px; }
  .holder { position: absolute; left: 44px; top: 40px; }
  .holder__name { font-size: 27px; font-weight: 400; line-height: 1.1; color: var(--brand-green); }
  .holder__name span { color: var(--brand-grey); font-weight: 300; }
  .holder__title { font-size: 12px; color: var(--brand-green); margin-top: 2px; }
  .holder__rule {
    position: absolute; left: 130px; top: 80px;
    width: 400px; height: 1.5px; background: var(--brand-green);
  }
  .contacts { position: absolute; left: 44px; top: 110px; list-style: none; }
  .contacts li {
    display: flex; align-items: center; gap: 10px;
    font-size: 12.5px; color: var(--ink-grey); line-height: 26px;
    white-space: nowrap;
  }
  .contacts svg { width: 16px; height: 16px; flex: none; }
  .wordmark {
    position: absolute; right: 44px; top: 206px;
    display: flex; align-items: center; gap: 10px;
    white-space: nowrap;
  }
  .wordmark__square { width: 16px; height: 16px; background: var(--brand-green); flex: none; }
  .wordmark__name { font-size: 22px; font-weight: 500; color: var(--brand-grey); letter-spacing: 0.2px; }
  .address {
    position: absolute; right: 44px; bottom: 40px;
    text-align: right; font-size: 14px; font-weight: 500; line-height: 1.3;
    color: var(--brand-green-deep);
  }

  /* Back */
  .card--back {
    background: var(--brand-green);
    display: flex; flex-direction: column; align-items: center; justify-content: center;
  }
  .back__name { font-size: 34px; font-weight: 600; color: #fff; letter-spacing: 0.3px; }
  .back__web {
    display: flex; align-items: center; gap: 18px; margin-top: 36px;
    font-size: 13px; letter-spacing: 3.5px; color: #fff;
  }
  .back__web i { display: block; width: 110px; height: 1.5px; background: var(--line-white); }
</style>
</head>
<body>
<main class="sheet">
  <section class="card card--front" aria-label="Business card front">
    <div class="holder">
      <p class="holder__name">Dorian <span>Pelkey</span></p>
      <p class="holder__title">Principle</p>
    </div>
    <div class="holder__rule"></div>

    <ul class="contacts">
      <li>
        <svg viewBox="0 0 16 16"><circle cx="8" cy="8" r="8" fill="var(--brand-green)"/><path d="M5.6 4.2l1.3 1.6-.7 1c.5 1 1.2 1.7 2.1 2.2l1-.7 1.6 1.3-.8 1.3c-2.6-.3-4.7-2.4-5-5z" fill="#fff"/></svg>
        917.806.3971
      </li>
      <li>
        <svg viewBox="0 0 16 16"><circle cx="8" cy="8" r="8" fill="var(--brand-grey)"/><rect x="4" y="5.2" width="8" height="5.6" rx="0.6" fill="none" stroke="#fff" stroke-width="1"/><path d="M4.3 5.6L8 8.5l3.7-2.9" fill="none" stroke="#fff" stroke-width="1"/></svg>
        info@bam-hvx.example
      </li>
      <li>
        <svg viewBox="0 0 16 16"><circle cx="8" cy="8" r="8" fill="var(--brand-green)"/><circle cx="8" cy="8" r="3.8" fill="none" stroke="#fff" stroke-width="1"/><path d="M4.2 8h7.6M8 4.2c-1.6 2.3-1.6 5.3 0 7.6M8 4.2c1.6 2.3 1.6 5.3 0 7.6" fill="none" stroke="#fff" stroke-width="0.9"/></svg>
        www.bam-hvx.example
      </li>
    </ul>

    <div class="wordmark">
      <span class="wordmark__square"></span>
      <span class="wordmark__name">Bluestone Advisory &amp; Mgmt</span>
    </div>

    <p class="address">348 West 71st Street,<br>9th FL New York,<br>NY 10010</p>

    <svg class="front__edge" viewBox="0 0 640 18" preserveAspectRatio="none" aria-hidden="true">
      <polygon points="0,0 190,0 180,18 0,18" fill="var(--brand-green)"/>
      <polygon points="196,0 204,0 194,18 186,18" fill="var(--brand-green)"/>
      <polygon points="210,0 640,0 640,18 200,18" fill="var(--brand-grey)"/>
    </svg>
  </section>

  <section class="card card--back" aria-label="Business card back">
    <p class="back__name">Bluestone Advisory &amp; Mgmt</p>
    <p class="back__web"><i></i>www.bam-hvx.example<i></i></p>
  </section>
</main>
</body>
</html>
```